Starvu Review Divorce Law Firm Folder Insert

We are a divorce law firm.

We need a flyer just like the one that is posted. For example, that allows for our Starvu reviews to be a good deed. We do like the coloring we will provide the image that goes on the bottom right. We are open to any design. Any thoughts people have, and unique designs are welcome were very happy with this example. However, we want people to know to have some background as to what would be the best option.

Again anything but again we do want the Starvu has to be the five stars in my logo has to be on there and the portion that says these different comments included

Target Market(s)

Divorce and Custody Clients

Industry/Entity Type

Legal

Requirements
Must have
• what must remain is the Starvu logo that large, and the five stars in the front in the back. What must be included is the Starvu reviews listed below. Not all of them must be used but no less than five must be used. At least one of the five

1.) “Worth the money!”
2.) “Simply the best”
3.) “So much knowledge and experience”
4.) “When life gets challenging, you want Marcus on your team!”
5.) “He made a painful divorce and custody, much easier to deal with”
6.) “Willingness to go the extra mile”
7.) “Respectful and caring”
8.) “I wouldn’t go with anyone else!”
Nice to have
• We are a divorce law firm in Harrisburg Pennsylvania. we need a Starvu review insert for our potential new clients folder. We need a hard insert flyer around 6 x 9 in height as similar possible to the one included as an attached, however we are open to any design. Since like the example so much the is a great guidepost.

We appreciate unique designs but have found one we have. To be very much to our liking. We are open to any other signs, but again. One example. Any thoughts people have, and unique designs are welcome were very happy with this example. However, we want people to know to have some background as to what would be the best option.

Attached you will find our logo, our shield by itself, the example card, and three images from which you should pick one.

one possibly to the photos can be included, but not aall three, included are three photos, only one should be used. Please pick one and use it
Should not have
• Look far off of a look that I too crazy

```html
<!DOCTYPE html>
<html lang="en">
<head>
<meta charset="UTF-8">
<title>Marcus R Whitfield – Starvu Reviews Insert</title>
<link href="https://fonts.googleapis.com/css2?family=Arvo:wght@700&family=Libre+Baskerville&family=Roboto:ital,wght@0,400;0,500;0,700;1,400&display=swap" rel="stylesheet">
<style>
  :root {
    --navy: #1b1f4b;
    --ink: #1a1a1a;
    --grey-dark: #3a3a3a;
    --star: #f2882a;
    --sky-top: #d5d4df;
    --sky-mid: #ddd3d6;
    --glow: #e6d0cc;
    --street: #cac7cc;
  }
  * { margin: 0; padding: 0; box-sizing: border-box; }
  html, body { width: 800px; height: 1200px; overflow: hidden; background: var(--sky-top); }
  .insert {
    position: relative;
    width: 800px;
    height: 1200px;
    overflow: hidden;
    font-family: "Roboto", Arial, sans-serif;
    color: var(--navy);
  }
  .backdrop {
    position: absolute;
    inset: 0;
    background:
      radial-gradient(ellipse 70% 30% at 30% 52%, rgba(255,255,255,0.35), transparent 70%),
      linear-gradient(180deg, var(--sky-top) 0%, var(--sky-mid) 38%, var(--glow) 55%, #d6d0d4 72%, var(--street) 100%);
  }
  .firm {
    position: absolute;
    left: 87px;
    top: 78px;
    display: flex;
    align-items: center;
    gap: 20px;
  }
  .firm-mark {
    width: 122px;
    height: 122px;
    background: var(--navy);
  }
  .firm-name {
    font-family: "Libre Baskerville", Georgia, serif;
    font-weight: 400;
    color: var(--navy);
    text-transform: uppercase;
    line-height: 1;
  }
  .firm-name .pre { display: block; font-size: 19px; letter-spacing: 0.5px; }
  .firm-name .name { display: block; font-size: 41px; margin-top: 10px; letter-spacing: -0.5px; }
  .tagline {
    position: absolute;
    top: 452px;
    left: 0;
    width: 800px;
    text-align: center;
  }
  .tagline .light { display: block; font-size: 36px; font-weight: 400; line-height: 1.2; }
  .tagline .strong {
    display: block;
    font-family: "Arvo", Georgia, serif;
    font-weight: 700;
    font-size: 44px;
    line-height: 1.3;
  }
  .testimonials {
    position: absolute;
    top: 690px;
    left: 60px;
    width: 680px;
    list-style: none;
    text-align: center;
  }
  .testimonial {
    font-size: 20px;
    font-style: italic;
    line-height: 36px;
    color: var(--navy);
  }
  .reviews {
    position: absolute;
    top: 920px;
    left: 0;
    width: 800px;
    text-align: center;
  }
  .reviews-lead { font-size: 22px; color: var(--ink); }
  .reviews-brand {
    display: block;
    font-size: 104px;
    font-weight: 500;
    color: var(--navy);
    line-height: 1.05;
    margin-top: 6px;
    letter-spacing: -2px;
  }
  .reviews-rating {
    display: flex;
    justify-content: center;
    align-items: center;
    gap: 10px;
    margin-top: 2px;
  }
  .reviews-label { font-size: 34px; font-weight: 700; color: var(--grey-dark); }
  .stars { display: flex; gap: 3px; }
  .stars svg { width: 20px; height: 20px; fill: var(--star); }
</style>
</head>
<body>
<main class="insert">
  <div class="backdrop" role="img" aria-label="Evening photograph of the state capitol dome and a monument along a lit boulevard"></div>

  <header class="firm">
    <div class="firm-mark"></div>
    <h1 class="firm-name">
      <span class="pre">The Law Office of</span>
      <span class="name">Marcus R Whitfield</span>
    </h1>
  </header>

  <section class="tagline">
    <span class="light">Providing</span>
    <span class="strong">Quality Legal Counsel</span>
    <span class="light">to Clients Across</span>
    <span class="strong">Central Pennsylvania</span>
  </section>

  <ul class="testimonials">
    <li class="testimonial">“Worth the money!”</li>
    <li class="testimonial">“So much knowledge and experience”</li>
    <li class="testimonial">“When life gets challenging, you want Marcus on your team!”</li>
    <li class="testimonial">“Willingness to go the extra mile”</li>
    <li class="testimonial">“I wouldn’t go with anyone else!”</li>
  </ul>

  <section class="reviews">
    <p class="reviews-lead">Check our testimonials at :</p>
    <span class="reviews-brand">Starvu</span>
    <div class="reviews-rating">
      <span class="reviews-label">Reviews</span>
      <span class="stars" aria-label="Five stars">
        <svg viewBox="0 0 24 24"><path d="M12 2l2.9 6.9 7.1.6-5.4 4.7 1.6 7.3L12 17.8 5.8 21.5l1.6-7.3L2 9.5l7.1-.6z"/></svg>
        <svg viewBox="0 0 24 24"><path d="M12 2l2.9 6.9 7.1.6-5.4 4.7 1.6 7.3L12 17.8 5.8 21.5l1.6-7.3L2 9.5l7.1-.6z"/></svg>
        <svg viewBox="0 0 24 24"><path d="M12 2l2.9 6.9 7.1.6-5.4 4.7 1.6 7.3L12 17.8 5.8 21.5l1.6-7.3L2 9.5l7.1-.6z"/></svg>
        <svg viewBox="0 0 24 24"><path d="M12 2l2.9 6.9 7.1.6-5.4 4.7 1.6 7.3L12 17.8 5.8 21.5l1.6-7.3L2 9.5l7.1-.6z"/></svg>
        <svg viewBox="0 0 24 24"><path d="M12 2l2.9 6.9 7.1.6-5.4 4.7 1.6 7.3L12 17.8 5.8 21.5l1.6-7.3L2 9.5l7.1-.6z"/></svg>
      </span>
    </div>
  </section>
</main>
</body>
</html>
```